Brisk Wire Services - Electrical

We need flyers for electrical services.
Areas of work include new builds, office fitouts, switchboard upgrades, installation of ceiling fans, powerpoint and downlight upgrades, home theatre and AV systems, all exterior and emergency work. Free quotes
We would like to see designs with the colour Red with a young and modern design. Licence No: 83146K must be included and call Leopold on 0418693027.

Colors
ec1f27

```html
<!DOCTYPE html>
<html lang="en">
<head>
<meta charset="utf-8">
<title>Brisk Wire Services – Electrical Flyer</title>
<link rel="stylesheet" href="https://fonts.googleapis.com/css2?family=Montserrat:wght@500;700;800;900&display=swap">
<style>
  :root {
    --brand-red: #ec1f27;
    --deep-red: #c5141b;
    --accent-yellow: #ffe500;
    --accent-orange: #f7a21b;
    --ink-black: #141414;
    --footer-grey: #3a3a3a;
    --white: #ffffff;
    --badge-gold: #e0b43a;
    --badge-dark: #2a2a2a;
  }
  * { box-sizing: border-box; margin: 0; padding: 0; }
  html, body { width: 857px; height: 1200px; overflow: hidden; background: #ffffff; }
  .flyer {
    position: relative;
    width: 857px;
    height: 1200px;
    overflow: hidden;
    background: linear-gradient(180deg, var(--brand-red) 0%, var(--deep-red) 100%);
    font-family: "Montserrat", Arial, sans-serif;
    color: var(--white);
  }
  .hero-photo {
    position: absolute;
    left: 0; top: 0;
    width: 857px; height: 560px;
    background: linear-gradient(135deg, #d9d4cc 0%, #b9b3ab 35%, #8c8f96 60%, #4a5a8a 100%);
  }
  .hero-wave {
    position: absolute;
    left: 0; top: 440px;
    width: 857px; height: 140px;
  }
  .guarantee-badge {
    position: absolute;
    left: 652px; top: 374px;
    width: 164px; height: 164px;
  }
  .brand-block {
    position: absolute;
    left: 26px; top: 552px;
    width: 400px;
  }
  .brand-name {
    font-weight: 900;
    font-size: 49px;
    line-height: 1;
    letter-spacing: 0.5px;
    text-transform: uppercase;
  }
  .brand-trade {
    font-weight: 800;
    font-size: 27px;
    line-height: 1.1;
    margin-top: 6px;
    color: var(--accent-yellow);
    text-transform: uppercase;
  }
  .brand-intro {
    margin-top: 26px;
    width: 350px;
    font-size: 15.5px;
    line-height: 22px;
    font-weight: 500;
  }
  .work-heading {
    position: absolute;
    left: 26px; top: 744px;
    font-size: 30px;
    font-weight: 700;
    color: var(--accent-yellow);
  }
  .work-list {
    position: absolute;
    left: 28px; top: 784px;
    list-style: none;
  }
  .work-list li {
    position: relative;
    padding-left: 24px;
    font-size: 19.5px;
    line-height: 32px;
    font-weight: 500;
  }
  .work-list li::before {
    content: "";
    position: absolute;
    left: 0; top: 9px;
    width: 14px; height: 14px;
    border-radius: 50%;
    background: var(--accent-yellow);
  }
  .contact-address {
    position: absolute;
    left: 27px; top: 1022px;
    width: 400px;
    font-size: 19.5px;
    line-height: 27px;
    font-weight: 500;
  }
  .licence-line {
    position: absolute;
    left: 27px; top: 1084px;
    font-size: 18.5px;
    font-weight: 700;
  }
  .about-copy {
    position: absolute;
    left: 446px; top: 580px;
    width: 392px;
    font-size: 15.2px;
    line-height: 22px;
    font-weight: 500;
    text-align: justify;
  }
  .about-copy .highlight { color: var(--accent-yellow); font-weight: 700; }
  .service-gallery {
    position: absolute;
    left: 446px; top: 841px;
    width: 403px;
    display: grid;
    grid-template-columns: 198px 198px;
    grid-template-rows: 133px 133px;
    gap: 6px 7px;
  }
  .gallery-tile { border: 2px solid rgba(255,255,255,0.85); }
  .tile-fan { background: linear-gradient(135deg, #e8e6e3, #9ea3a8); }
  .tile-aircon { background: linear-gradient(135deg, #f1f1f1, #c7c9cc); }
  .tile-switchboard { background: linear-gradient(135deg, #8b8f96, #d26b3a); }
  .tile-cabling { background: linear-gradient(135deg, #d8d8d8, #e0522f); }
  .call-bar {
    position: absolute;
    left: 0; top: 1123px;
    width: 857px; height: 77px;
    background: linear-gradient(180deg, var(--footer-grey) 0%, var(--ink-black) 100%);
    display: flex;
    align-items: center;
    justify-content: center;
    font-size: 35px;
    font-weight: 800;
    letter-spacing: 0.5px;
    text-transform: uppercase;
  }
  .call-bar .phone-number { color: var(--accent-yellow); margin-left: 12px; }
</style>
</head>
<body>
<main class="flyer">
  <div class="hero-photo" role="img" aria-label="Electrician in a red hard hat holding pliers in front of an open switchboard"></div>

  <svg class="hero-wave" viewBox="0 0 857 140" preserveAspectRatio="none" aria-hidden="true">
    <path d="M0 60 C 180 20, 360 110, 520 100 C 650 92, 760 40, 857 20 L857 140 L0 140 Z" fill="var(--accent-orange)"/>
    <path d="M0 66 C 180 30, 360 116, 520 108 C 650 100, 760 52, 857 34 L857 140 L0 140 Z" fill="var(--accent-yellow)"/>
    <path d="M0 76 C 180 42, 360 126, 520 118 C 650 110, 760 66, 857 48 L857 140 L0 140 Z" fill="var(--brand-red)"/>
  </svg>

  <svg class="guarantee-badge" viewBox="0 0 164 164" aria-hidden="true">
    <circle cx="82" cy="82" r="80" fill="var(--badge-gold)"/>
    <circle cx="82" cy="82" r="64" fill="var(--badge-dark)"/>
    <circle cx="82" cy="82" r="40" fill="var(--badge-gold)"/>
  </svg>

  <section class="brand-block">
    <h1 class="brand-name">Brisk Wire</h1>
    <p class="brand-trade">Services</p>
    <p class="brand-intro">Licensed local electricians delivering safe, tidy and reliable work for homes and businesses.</p>
  </section>

  <h2 class="work-heading">Areas of work</h2>
  <ul class="work-list">
    <li>New builds</li>
    <li>Office fitouts</li>
    <li>Switchboard upgrades</li>
    <li>Installation of ceiling fans</li>
    <li>Powerpoint and downlight upgrades,</li>
    <li>Home theatre and AV systems,</li>
    <li>All exterior and emergency work</li>
  </ul>

  <p class="contact-address">Unit 4, 18 Harbour Lane,<br>Northgate NSW 2150</p>
  <p class="licence-line">Licence No: 83146K</p>

  <section class="about-copy">
    <p>Brisk Wire Services brings a young, modern approach to every electrical job. From the first call to the final test, our team works cleanly, explains each step and finishes on time. <span class="highlight">Call today for your free quote with no obligation – we inspect, advise and price your job on the spot.</span></p>
    <p>We use quality parts, follow every safety standard and back our work with a full satisfaction guarantee. From a single powerpoint to a complete fitout, no job is too big or too small.</p>
  </section>

  <div class="service-gallery">
    <div class="gallery-tile tile-fan" role="img" aria-label="Electrician installing a ceiling fan"></div>
    <div class="gallery-tile tile-aircon" role="img" aria-label="Technician servicing a wall-mounted unit"></div>
    <div class="gallery-tile tile-switchboard" role="img" aria-label="Electricians working at a switchboard"></div>
    <div class="gallery-tile tile-cabling" role="img" aria-label="Orange conduit cabling inside a wall box"></div>
  </div>

  <footer class="call-bar">Call Leopold on <span class="phone-number">0418693027</span></footer>
</main>
</body>
</html>
```